Digital Marketing Website Design

I need the homepage designed for my new digital marketing agency I am starting. The main goal for this homepage is to drive people to make an appointment for me to discuss their upcoming projects. Here are some examples of the layouts that I would like to emulate.
https://www.tallorchard.com/
https://www.webmerchantry.com/
https://talewick.com/
https://drmevorran.com/
https://www.neatlynestled.org/
My main focus is to attract leads that need help with running digital ads such as Chatterbook ads and Quorix Ads. I do offer other services like SEO and other things but the main focus is digital Ads.
The final design should communicate Ember Pixelry is a Digital marketing strategist building predictable revenue for small businesses through digital ads, email and marketing automation.
Target Market(s)
30-55, business owners, income 100K+, ecommerce companies, etc.
Industry/Entity Type
Digital Marketing
Number of Pages Required
2 page
Requirements
Must have
- An appealing look and feel set to drive people to make an appointment.
There needs to be a call to action button in the far right of the navigation
The same call to action in the navigation needs to be in each section on the homepage.
I need the homepage and an about us page.

```html
<!DOCTYPE html>
<html lang="en">
<head>
<meta charset="utf-8">
<title>Ember Pixelry – Digital Ads for Small Businesses</title>
<link rel="stylesheet" href="https://fonts.googleapis.com/css2?family=Montserrat:wght@500;600;700;800&family=Open+Sans:wght@400;600&display=swap">
<style>
:root{
  --orange:#f47a20;
  --orange-dark:#e2650c;
  --ink:#2b2b2b;
  --body:#6b6b6b;
  --light:#f4f4f4;
  --white:#ffffff;
  --footer:#1d1d1d;
  --footer-text:#b9b9b9;
}
*{box-sizing:border-box;margin:0;padding:0}
html,body{width:1200px;height:2536px;overflow:hidden}
body{font-family:"Open Sans",Arial,sans-serif;color:var(--body);background:var(--white);position:relative}
h1,h2,h3,.nav,.btn,.brand{font-family:"Montserrat",Arial,sans-serif}
.btn{display:inline-block;font-weight:700;font-size:14px;letter-spacing:.5px;text-transform:uppercase;padding:14px 28px;border-radius:2px;text-decoration:none}
.btn-orange{background:var(--orange);color:var(--white)}
.btn-white{background:var(--white);color:var(--ink)}

/* Hero */
.hero{position:absolute;top:0;left:0;width:1200px;height:740px;background:linear-gradient(160deg,#4a4a4a 0%,#2e2e2e 45%,#3b3b3b 100%)}
.hero-photo{position:absolute;inset:0;background:radial-gradient(ellipse at 70% 35%,rgba(120,120,120,.55),transparent 60%),radial-gradient(ellipse at 20% 60%,rgba(90,90,90,.5),transparent 55%)}
.topbar{position:absolute;top:44px;left:100px;right:100px;display:flex;align-items:center;justify-content:space-between}
.brand{display:flex;align-items:center;gap:10px;font-weight:800;font-size:24px;color:var(--white);text-transform:uppercase;letter-spacing:1px}
.brand-dot{width:16px;height:16px;background:var(--orange)}
.nav{display:flex;align-items:center;gap:36px}
.nav .nav-link{color:var(--white);font-size:13px;font-weight:600;text-decoration:none;text-transform:uppercase}
.nav .btn-white{color:var(--ink);font-size:13px;padding:13px 24px}
.hero-copy{position:absolute;top:270px;left:0;width:1200px;text-align:center;color:var(--white)}
.hero-copy h1{font-weight:800;font-size:38px;line-height:46px;text-transform:uppercase;letter-spacing:1px}
.hero-copy p{margin:20px auto 0;width:520px;font-size:15px;line-height:24px;color:#d6d6d6}
.hero-copy .btn{margin-top:26px}
.badges{position:absolute;top:590px;left:0;width:1200px;display:flex;justify-content:center;align-items:center;gap:64px}
.badge{background:rgba(255,255,255,.85)}
.badge.round{width:88px;height:88px;border-radius:50%}
.badge.wide{width:160px;height:60px}
.badge.tall{width:70px;height:90px}

/* How it works */
.how{position:absolute;top:740px;left:0;width:1200px;height:370px;text-align:center}
.section-title{font-weight:700;font-size:40px;color:var(--ink);text-transform:uppercase;letter-spacing:1px}
.how .section-title{margin-top:84px}
.accent{width:24px;height:24px;border-radius:50%;background:var(--orange);margin:20px auto 0}
.how p{width:880px;margin:28px auto 0;font-size:15px;line-height:27px}

/* Process band */
.process{position:absolute;top:1110px;left:0;width:1200px;height:370px;display:flex}
.process-photo{width:480px;height:370px;background:linear-gradient(135deg,#dcdcdc 0%,#bfc3c8 55%,#8f9399 100%)}
.process-body{flex:1;background:var(--orange);color:var(--white);padding:54px 80px 0 70px}
.process-body h2{font-weight:800;font-size:34px;text-transform:uppercase;letter-spacing:1px}
.steps{list-style:none;margin-top:24px}
.steps li{display:flex;gap:14px;font-size:15px;line-height:22px;margin-bottom:12px}
.steps svg{flex:none;margin-top:3px}
.process-body p{font-size:15px;line-height:24px;margin-top:12px}
.process-body .btn{margin-top:14px;padding:11px 24px;font-size:13px}

/* Testimonials */
.reviews{position:absolute;top:1480px;left:0;width:1200px;height:780px;background:var(--light);text-align:center}
.reviews .section-title{margin-top:144px}
.cards{display:flex;justify-content:center;gap:40px;margin-top:64px}
.card{width:300px;height:370px;background:var(--white);box-shadow:0 2px 10px rgba(0,0,0,.08);padding:0 30px;text-align:left;position:relative}
.avatar{width:82px;height:82px;border-radius:50%;background:linear-gradient(135deg,#c9cdd2,#9aa0a7);border:4px solid var(--white);margin:26px auto 0}
.card h3{text-align:center;color:var(--orange);font-weight:600;font-size:19px;margin-top:16px}
.card .role{text-align:center;font-size:13px;color:#999;margin-top:4px}
.card p{font-size:14px;line-height:24px;margin-top:26px}
.arrows{display:flex;justify-content:center;gap:28px;margin-top:34px}

/* Footer */
.footer{position:absolute;top:2260px;left:0;width:1200px;height:276px;background:var(--footer);color:var(--footer-text);font-size:14px}
.footer-cols{position:absolute;top:54px;left:128px;display:flex}
.footer h3{color:var(--white);font-weight:700;font-size:15px;margin-bottom:20px}
.col-contact{width:232px}
.col-pages{width:240px}
.contact-line{display:flex;align-items:center;gap:12px;margin-bottom:14px}
.page-links{display:grid;grid-template-columns:100px 100px;row-gap:10px}
.useful li{list-style:none;margin-bottom:10px}
.social{position:absolute;top:92px;right:130px;display:flex;gap:12px}
.social span{width:26px;height:26px;border-radius:50%;background:var(--white)}
.footer-base{position:absolute;top:214px;left:128px;right:130px;display:flex;justify-content:space-between;align-items:center;border-top:1px solid #333;padding-top:20px;font-size:13px}
.footer .brand{font-size:22px}
</style>
</head>
<body>

<header class="hero">
  <div class="hero-photo" role="img" aria-label="Darkened photo of a team working in an office"></div>
  <div class="topbar">
    <div class="brand"><span class="brand-dot"></span>Ember Pixelry</div>
    <nav class="nav">
      <a class="nav-link" href="#">Home</a><a class="nav-link" href="#">About</a><a class="nav-link" href="#">Contact</a>
      <a class="btn btn-white" href="#">Schedule Appointment</a>
    </nav>
  </div>
  <div class="hero-copy">
    <h1>We built profitable ad campaigns<br>for small businesses</h1>
    <p>Predictable revenue through digital ads, email and marketing automation built for your growth.</p>
    <a class="btn btn-orange" href="#">Schedule Appointment</a>
  </div>
  <div class="badges">
    <span class="badge round"></span>
    <span class="badge wide"></span>
    <span class="badge tall"></span>
    <span class="badge round"></span>
  </div>
</header>

<section class="how">
  <h2 class="section-title">How it works</h2>
  <div class="accent"></div>
  <p>At Ember Pixelry we know that you want to grow a profitable business. In order to do that, you need a strong system that can predictably bring in sales every month. The problem is there is so much out there to wade through and so many people telling you what you should do, which makes you feel frustrated and stuck. We believe that businesses with great products should get the customers they deserve. We understand that frustration, which is why we are here to help you break through the noise and create a system that fits your goals and your budget.</p>
</section>

<section class="process">
  <div class="process-photo" role="img" aria-label="Photo of hands typing on a laptop at a desk"></div>
  <div class="process-body">
    <h2>Here's how we do it:</h2>
    <ul class="steps">
      <li><svg width="16" height="16" viewBox="0 0 16 16"><circle cx="8" cy="8" r="7.5" fill="#fff"/><path d="M4.5 8.2l2.3 2.3 4.7-4.9" stroke="#f47a20" stroke-width="2" fill="none"/></svg>Schedule an appointment to go through the current state of your business and where you want to be next.</li>
      <li><svg width="16" height="16" viewBox="0 0 16 16"><circle cx="8" cy="8" r="7.5" fill="#fff"/><path d="M4.5 8.2l2.3 2.3 4.7-4.9" stroke="#f47a20" stroke-width="2" fill="none"/></svg>Pick a plan and enjoy the sales increase.</li>
      <li><svg width="16" height="16" viewBox="0 0 16 16"><circle cx="8" cy="8" r="7.5" fill="#fff"/><path d="M4.5 8.2l2.3 2.3 4.7-4.9" stroke="#f47a20" stroke-width="2" fill="none"/></svg>Work with our team to build out your customer journey and selling system.</li>
    </ul>
    <p>So schedule your appointment today. Avoid the headaches of wasted ad spend and get the predictable revenue your business needs to grow.</p>
    <a class="btn btn-white" href="#">Schedule Appointment</a>
  </div>
</section>

<section class="reviews">
  <h2 class="section-title">What others are saying</h2>
  <div class="accent"></div>
  <div class="cards">
    <article class="card">
      <div class="avatar" role="img" aria-label="Client portrait"></div>
      <h3>Sample Client</h3>
      <div class="role">Satisfied Client</div>
      <p>Our ads finally pay for themselves. The team built a clear plan, tracked every dollar and doubled our monthly sales in a short time.</p>
    </article>
    <article class="card">
      <div class="avatar" role="img" aria-label="Client portrait"></div>
      <h3>Sample Client</h3>
      <div class="role">Satisfied Client</div>
      <p>Working with them took the guesswork out of marketing. We now have steady leads each week and an email system that runs itself.</p>
    </article>
    <article class="card">
      <div class="avatar" role="img" aria-label="Client portrait"></div>
      <h3>Sample Client</h3>
      <div class="role">Satisfied Client</div>
      <p>Honest advice, fast results and great support. Our online store grew more this year than in the three years before combined.</p>
    </article>
  </div>
  <div class="arrows">
    <svg width="14" height="14" viewBox="0 0 14 14"><path d="M9 2L4 7l5 5" stroke="#333" stroke-width="2" fill="none"/></svg>
    <svg width="14" height="14" viewBox="0 0 14 14"><path d="M5 2l5 5-5 5" stroke="#333" stroke-width="2" fill="none"/></svg>
  </div>
</section>

<footer class="footer">
  <div class="footer-cols">
    <div class="col-contact">
      <h3>Contact us</h3>
      <div class="contact-line"><svg width="14" height="14" viewBox="0 0 24 24"><path fill="#b9b9b9" d="M6.6 10.8a15 15 0 006.6 6.6l2.2-2.2c.3-.3.7-.4 1-.2 1.1.4 2.3.6 3.6.6.6 0 1 .4 1 1V20c0 .6-.4 1-1 1A17 17 0 013 4c0-.6.4-1 1-1h3.5c.6 0 1 .4 1 1 0 1.3.2 2.5.6 3.6.1.3 0 .7-.2 1z"/></svg>(123) 456-7890</div>
      <div class="contact-line"><svg width="14" height="14" viewBox="0 0 24 24"><path fill="#b9b9b9" d="M2 5h20v14H2z"/><path d="M2 5l10 8 10-8" stroke="#1d1d1d" stroke-width="2" fill="none"/></svg>hello@emberpixelry.com</div>
    </div>
    <div class="col-pages">
      <h3>Pages</h3>
      <div class="page-links"><span>Home</span><span>Blog</span><span>About</span><span>Contact</span><span>Services</span><span></span><span>Resources</span></div>
    </div>
    <div>
      <h3>Useful links</h3>
      <ul class="useful"><li>Starting a small online store</li><li>Social ad guides</li><li>Email automation information</li></ul>
    </div>
  </div>
  <div class="social"><span></span><span></span><span></span></div>
  <div class="footer-base">
    <span>Copyright © 2024 Ember Pixelry &nbsp;|&nbsp; Terms of Service &nbsp;|&nbsp; Privacy Policy</span>
    <div class="brand"><span class="brand-dot"></span>Ember Pixelry</div>
  </div>
</footer>

</body>
</html>
```